VESTRA電子書籍 表紙発注書

【依頼概要】

<サブタイトル>

小さな会社や個人事業でもできる!

<書籍タイトル>

数字が苦手な 店主のための
【看板づくり手帖】

※ターゲットの目にすぐ入る様に(小さな会社)(個人事業)(ネットに弱い)を目立つ様にお願いします。
※電子書籍なので表示される際の画像が小さいため、タイトルもできるだけ視認しやすい文字でお願いします。

<オビ部分>

ホームページを作る前に
必ずお読みください。

読者限定プレゼント付
●思わずポチッと押したくなる!
【段階別】キャッチコピーの作り方
●真似するだけでOK!
【ランディングページのテンプレート】

※プレゼントは目立つ様にお願いします。

<著者>

WEB集客のしくみ作りの専門家
森田 サキ

※著者似顔絵をどちらか使ってください。

<読者ターゲット層>
・40代~50代の、小規模企業の経営者・個人事業経営者・個人起業家

<イメージ>
・色の指定などはありません。
もし自分が起業する時なら、どんな表紙に目が止まるか考えてみていただけると嬉しいです。

・ビジネス書ではありますが、ターゲットはネットやパソコンに苦手意識を持っている経営者の方なので、また女性の起業家さんにも見て欲しいので、ちゃんとした雰囲気はありつつも、あまり硬くなく、自分でもできそうかなー、と思わせる様な雰囲気が出るといいなと思っています。
よろしくお願いいたします。

※著者似顔絵2点添付します。どちらかをお使いください。
※写真・イラスト素材購入の際は別途お支払いします。 その場合は、小サイズ画像で大丈夫です。

※参考資料として、まだ未完成ですが原稿を添付します。
パスワードがありますのでこちらで開いてください。

▶︎PDFを開く時のパスワード: demo1

《追記1》必ずご覧ください。
↓ ↓ ↓
書籍のタイトルとオビの文言をを変更しました。
申し訳ありませんが、こちらを必ずご確認ください。

(すでに提案をくださった方は、そのままのデザインで検討させていただきますので、再提出はしなくて大丈夫です。採用になった場合のみ変更のご依頼をさせていただきますが、その際は報酬をプラスさせていただきます※9/15日朝7時30分までに提案くださった方)

《変更内容》
<書籍タイトル>
帳簿が苦手な 店主のための
「街角で商売」

※ターゲットの目にすぐ入る様に(小さな会社)(個人事業)(ウェブに弱い)を目立つ様にお願いします。

<オビ部分>
※この本を読むまでは
ホームページは作らないでください。

▶︎参考本文(未完成)は新しい方(ファイル名:【原稿】こちらをご覧ください)
をご覧ください」
▶︎▶︎PDFファイルパスワード demo2
《追記2》
追記1にて一部変更をさせていただきましたが、
追記1の《変更内容》以外は最初の依頼内容通りなので、再度ご確認ください。

あと、少し気になったのですが、著者の似顔絵はメインビジュアルに使わなくて大丈夫です。名前の横にひっそりとつかう程度でいいかと思います。
もちろん、何か意図を持って使いたいという場合はご提案大歓迎です^ ^

▶︎必要な構成要素を再度まとめますね。
(読者ターゲットや希望デザインについては最初の依頼内容をご確認ください)
ーーーーーーーーーーーーーーーーーーー
<文字>
小さな会社や個人事業でもできる!

帳簿が苦手な 店主のための
「街角で商売」

※この本を読むまでは
ホームページは作らないでください。

読者限定プレゼント付
●思わずポチッと押したくなる!
【段階別 キャッチコピーの作り方】
●真似するだけでOK!
【ランディングページのテンプレート】

WEB集客のしくみ作りの専門家
森田 サキ

<画像>
著者似顔絵(メインビジュアルには使わなくていいいです)

※その他、写真・イラストの使用はお任せ

ーーーーーーーーーーーーーーーーーーー

こちらの説明不足のため誤解を招いてしまい、たいへん申し訳ございませんでした。

誰のための何の本ななのか、スマホでVestraを見た時でもはっきりわかるスッキリしたデザインがよかったです。また、こちらの要望通りに、ウェブが苦手な人や女性も、ついポチッと押してしまいそうなデザインでした。

選考には、20人ほどの方から意見をいただいたのですが、やはりはっきり文字が読み取れるものが人気が高かったです。
なるほどなぁ、と思ったのは、少しデザインの知識がある人(私を含め)と、とくにこだわりのない普通の人たちとでは、見る視点が違うのか、少し意見が別れました。読者目線がやはり大事ですね。

たくさんのご提案をいただき、本当にありがとうございました。

中には、さすがプロっぽいと思わせる作品や、手間をかけて作ってくださったと思われる作品もあり、本当にありがたく、また選考もかなり迷いました。

提案してくださった皆様、本当にありがとうございました。

```html
<!DOCTYPE html>
<html lang="ja">
<head>
<meta charset="utf-8">
<title>帳簿が苦手な 店主のための 街角で商売</title>
<link href="https://fonts.googleapis.com/css2?family=Noto+Sans+JP:wght@500;700;900&family=Noto+Serif+JP:wght@600&display=swap" rel="stylesheet">
<style>
  :root{
    --yellow:#fff100;
    --red:#e3221b;
    --blue:#1c7fd2;
    --ink:#1a1a1a;
    --paper:#ffffff;
  }
  html,body{margin:0;padding:0;overflow:hidden;}
  body{width:752px;height:1200px;}
  .cover{
    position:relative;width:752px;height:1200px;overflow:hidden;
    background:var(--paper);
    font-family:"Noto Sans JP",sans-serif;color:var(--ink);
  }
  .cover__band{position:absolute;left:0;top:0;width:752px;height:745px;background:var(--yellow);}

  .lead{position:absolute;left:95px;top:30px;white-space:nowrap;font-weight:900;}
  .lead__accent{color:var(--red);font-size:66px;letter-spacing:-1px;}
  .lead__rest{font-size:40px;margin-left:6px;}

  .title{
    position:absolute;writing-mode:vertical-rl;font-weight:900;
    font-size:188px;line-height:1;letter-spacing:-8px;
  }
  .title--top{left:475px;top:145px;color:var(--ink);}
  .title--bottom{left:475px;top:755px;color:var(--red);}

  .subtitle{position:absolute;left:130px;top:135px;width:350px;text-align:center;font-weight:900;line-height:1.1;}
  .subtitle__line1{color:var(--blue);font-size:58px;}
  .subtitle__line2{color:var(--blue);font-size:72px;-webkit-text-stroke:2px var(--paper);paint-order:stroke fill;}
  .subtitle__line3{font-size:58px;}

  .author-role{
    position:absolute;left:24px;top:240px;width:42px;height:420px;background:var(--red);
    color:var(--paper);writing-mode:vertical-rl;font-weight:700;font-size:25px;
    display:flex;align-items:center;justify-content:center;letter-spacing:1px;
  }
  .author-name{
    position:absolute;left:74px;top:245px;writing-mode:vertical-rl;
    font-family:"Noto Serif JP",serif;font-weight:600;font-size:38px;letter-spacing:4px;
  }
  .author-portrait{position:absolute;left:22px;top:670px;width:78px;height:78px;border-radius:50%;background:linear-gradient(#f6d7c0,#c89a7a);}
  .scene{position:absolute;left:150px;top:470px;width:330px;height:280px;border-radius:12px;background:linear-gradient(160deg,#9fb8d6,#3f5878);}

  .pitch{position:absolute;top:790px;height:400px;writing-mode:vertical-rl;}
  .pitch--body{left:285px;width:190px;font-size:24px;font-weight:500;line-height:1.5;}
  .pitch--key{left:25px;width:240px;font-size:31px;font-weight:900;color:var(--red);line-height:1.4;}

  .warning{
    position:absolute;left:672px;top:785px;height:410px;writing-mode:vertical-rl;
    font-size:24px;font-weight:700;line-height:1.5;
  }
</style>
</head>
<body>
  <main class="cover">
    <div class="cover__band"></div>

    <p class="lead" style="margin:0"><span class="lead__accent">帳簿が苦手な</span><span class="lead__rest">店主のための</span></p>

    <h1 class="title title--top" style="margin:0">街角で</h1>
    <div class="title title--bottom">商売</div>

    <div class="subtitle">
      <div class="subtitle__line1">小さな会社や</div>
      <div class="subtitle__line2">個人事業</div>
      <div class="subtitle__line3">でもできる！</div>
    </div>

    <div class="author-role">ウェブ集客のしくみ作り専門家</div>
    <div class="author-name">森田 サキ</div>
    <div class="author-portrait" role="img" aria-label="著者の似顔絵イラスト"></div>

    <div class="scene" role="img" aria-label="パソコンを囲んで話し合うビジネスパーソンのイラスト"></div>

    <p class="pitch pitch--body" style="margin:0">あなたがインターネットで集客できないのは、ホームページを更新しなかったからでも、SNSに毎日投稿していないからでも、「いいね」が少ないからでもありません。</p>
    <p class="pitch pitch--key" style="margin:0">それは、「ウェブから売り上げが上がるまでの仕組み」＝「ウェブ集客の仕組み」がないから売り上げが上がらないだけなのです。</p>

    <p class="warning" style="margin:0">この本を読むまでは<br>ホームページは作らないでください。</p>
  </main>
</body>
</html>
```